EPS Recycling Rpt

Our annual recycling rate report needs a tune up. Our organization helps faciltate expanded polystyrene (EPS) recycling and this 4-page report highlights growth trends and useful information to help readers understand the dynamics of EPS recycling. We need a designer that can recreate the brochure we've published over the past several years with some minor adjustments to accomodate new content.

A PDF of the 2012 report is attached. Header text should reflect 2013 in all cases. Please pay close attention to the new placement of the copy as indicated in the Word file (also attached) as it has been significantly modified from the 2012 version. The color pallette for our branding is provided. Contact us with any questions.

```html
<!DOCTYPE html>
<html lang="en">
<head>
<meta charset="utf-8">
<title>2013 EPS Recycling Rate Report</title>
<link href="https://fonts.googleapis.com/css2?family=Raleway:wght@400;500&family=Open+Sans:wght@400&display=swap" rel="stylesheet">
<style>
  :root {
    --slate: #5f87a0;
    --slate-text: #6f92a8;
    --brown: #5c2e1a;
    --title-olive: #94a23a;
    --paper: #ffffff;
    --grid: #8fb0c4;
  }
  html, body { margin: 0; padding: 0; }
  body {
    width: 848px; height: 1200px; overflow: hidden;
    background: var(--paper); position: relative;
    font-family: "Open Sans", Arial, sans-serif;
  }
  .top-rule { position: absolute; top: 0; left: 0; width: 848px; height: 15px; background: var(--slate); }

  .org-name {
    position: absolute; left: 42px; top: 66px; margin: 0;
    display: flex; align-items: center; gap: 10px;
    font-family: "Raleway", Arial, sans-serif; font-weight: 500; font-size: 17px;
    color: var(--slate);
  }
  .org-name .square { width: 12px; height: 12px; background: var(--slate); }

  .report-title {
    position: absolute; right: 42px; top: 42px; margin: 0; text-align: right;
    font-family: "Raleway", Arial, sans-serif; font-weight: 400; font-size: 32px;
    line-height: 36px; color: var(--title-olive); letter-spacing: 0.5px;
  }

  .section-heading {
    position: absolute; left: 301px; margin: 0;
    font-family: "Raleway", Arial, sans-serif; font-weight: 500; font-size: 16.5px;
    color: var(--slate); letter-spacing: 0.4px;
  }
  .body-copy {
    position: absolute; left: 301px; width: 508px; margin: 0;
    font-size: 13.9px; line-height: 19.2px; color: var(--slate-text);
  }
  .h-stronger { top: 160px; }
  .p-intro { top: 196px; }
  .h-method { top: 694px; }
  .p-method-1 { top: 735px; }
  .p-method-2 { top: 900px; }

  .chart-panel { position: absolute; left: 40px; top: 363px; width: 767px; height: 288px; background: var(--slate); }
  .chart-panel svg { display: block; }
  .chart-panel text { fill: #ffffff; font-family: "Raleway", Arial, sans-serif; }
</style>
</head>
<body>
  <div class="top-rule"></div>

  <p class="org-name"><span class="square"></span>Foam Recovery Council</p>

  <h1 class="report-title">2013 EPS RECYCLING<br>RATE REPORT</h1>

  <h2 class="section-heading h-stronger">EPS RECYCLING: STRONGER THAN EVER</h2>
  <p class="body-copy p-intro">As shown in Figure 2, the EPS packaging recycling rate percentage continues to grow steadily, showing a dependable track record to deliver consistent results. In fact, when comparing rigid, durable PS and other grade materials, EPS post-consumer and post-commercial recycling represent 47% of all post-use polystyrene recycled in the U.S. and is one of the highest within the plastics family.</p>

  <div class="chart-panel">
    <svg width="767" height="288" viewBox="0 0 767 288" role="img" aria-label="Line chart: post-consumer EPS recycling, millions of pounds, 1990 to 2013">
      <g stroke="var(--grid)" stroke-width="1">
        <line x1="80" y1="33" x2="743" y2="33"/>
        <line x1="80" y1="61" x2="743" y2="61"/>
        <line x1="80" y1="89" x2="743" y2="89"/>
        <line x1="80" y1="117" x2="743" y2="117"/>
        <line x1="80" y1="144" x2="743" y2="144"/>
        <line x1="80" y1="172" x2="743" y2="172"/>
        <line x1="80" y1="200" x2="743" y2="200"/>
        <line x1="80" y1="228" x2="743" y2="228"/>
        <line x1="80" y1="256" x2="743" y2="256"/>
      </g>
      <g font-size="15">
        <text x="53" y="38">80</text><text x="53" y="66">70</text><text x="53" y="94">60</text>
        <text x="53" y="122">50</text><text x="53" y="149">40</text><text x="53" y="177">30</text>
        <text x="53" y="205">20</text><text x="53" y="233">10</text><text x="53" y="261">0</text>
      </g>
      <text transform="translate(31 148) rotate(-90)" font-size="13" text-anchor="middle" letter-spacing="0.6">MILLIONS OF POUNDS RECYCLED</text>
      <text x="400" y="54" font-size="13.5" text-anchor="middle" letter-spacing="0.3">FIGURE 2: POST-CONSUMER EPS RECYCLING RATE HISTORY (1990-2013)</text>
      <g font-size="13" text-anchor="middle">
        <text x="105.5" y="276">1990</text><text x="156.5" y="276">1992</text><text x="207.5" y="276">1994</text>
        <text x="258.5" y="276">1996</text><text x="309.5" y="276">1998</text><text x="360.5" y="276">2000</text>
        <text x="411.5" y="276">2002</text><text x="462.5" y="276">2004</text><text x="513.5" y="276">2006</text>
        <text x="564.5" y="276">2008</text><text x="615.5" y="276">2010</text><text x="666.5" y="276">2012</text>
        <text x="717.5" y="276">2013</text>
      </g>
      <polyline fill="none" stroke="#ffffff" stroke-width="1.6"
        points="105.5,246.2 156.5,197.4 207.5,187.6 258.5,193.2 309.5,201.6 360.5,186.3 411.5,182.1 462.5,184.9 513.5,165.3 564.5,161.1 615.5,151.4 666.5,152.8 717.5,52.3"/>
      <g fill="#ffffff">
        <circle cx="105.5" cy="246.2" r="4"/><circle cx="156.5" cy="197.4" r="4"/><circle cx="207.5" cy="187.6" r="4"/>
        <circle cx="258.5" cy="193.2" r="4"/><circle cx="309.5" cy="201.6" r="4"/><circle cx="360.5" cy="186.3" r="4"/>
        <circle cx="411.5" cy="182.1" r="4"/><circle cx="462.5" cy="184.9" r="4"/><circle cx="513.5" cy="165.3" r="4"/>
        <circle cx="564.5" cy="161.1" r="4"/><circle cx="615.5" cy="151.4" r="4"/><circle cx="666.5" cy="152.8" r="4"/>
        <circle cx="717.5" cy="52.3" r="4"/>
      </g>
    </svg>
  </div>

  <h2 class="section-heading h-method">REPORT METHODOLOGY</h2>
  <p class="body-copy p-method-1">The methodology for this annual report focuses on the development of a numerator and denominator figure. Recycled pounds, used as the numerator in the recycling rate equation, are based on an annual survey of post-consumer and post-commercial plastic recyclers (including EPS industry manufacturing facilities ) and reflect the quantity of EPS recycled each year. Recycled pounds were counted at the stage where materials enter a reclamation facility (as opposed to net material recycled into resin or products) or were shipped for recycling outside the U.S.</p>
  <p class="body-copy p-method-2">Due to supply distribution chains and multiple end-use applications for EPS, a fixed number for EPS packaging generated each year is not available. Other manufacturing streams include building and construction applications, sporting goods and other durable products. As a proxy, resin sales data as reported for custom moded applications are used as the denominator in the recycling rate equations, which were provided by the National Polymer Council (NPC) Resin Producers’ Statistics Group. NPC reports are compiled from primary data reported by resin producers to the professional services firm of Halden Data Partners, LLC. This does not account for non-U.S. resin sales which may offset the quantities reported by U.S. resin suppliers sold into custom molding facilities for non-packaging applications.</p>
</body>
</html>
```